Web Design Job: Condo Debts Collection Business needs a Web Design

I need a site for a client, who works with condo debts collection, and ensure all revenues provided by condo fees will be always available to the building manager of condo on a specific date, regardless of defaults.
I have the visual identity (logo, slogan and colors) of the company, and some requirements on layout (kind of slider, menu options, phone number on a noble position, etc) - maybe I can do a sketch, but I like the idea of give some freedom to designer.

*** PLEASE, we have no interest in templates. We want something new***

Reason: We need something new, different and exclusive. We do not want anything that looks like a "template". Thanks.

Target Market(s)

I have two targets for this design:
- Condominium's building manager. This target is looking for a solution to overdue debts on it's condo.
- Residents on condominiums. This target wants to live in a better place, where their neighbors pay their condominium fees on time.

Industry/Entity Type

Business

Number of Pages Required

1 page

Requirements
Must have
• - Slider with title, some short text related, a nice image (I prefer happy and/or peaceful family, people doing business, happy friends, and so on).
• - I have a special attention to menu. I'm looking for one I can have a nice effect, more elegant, charming, kind of innovative.
• - Phone number on the top (or clearly visible).
• - Member log in area or icon on the top (or clearly visible).
• - News/articles area.
• - Modern fonts, with good quality, sans-serif on areas where reading is more intensive (prefer Google web-fonts).
• - Colors specified on attached files.
Nice to have
• - Clear background color, cause it's better to read larger texts (like articles). Dark backgrounds makes reading difficult.
• - A site with effects (like shadows, lines, curves, gradients, lights) is usually pretty.
• - I pay attention on beautiful footers.
Should not have
• - Images with a lot of money (I don't sell richness, I sell tranquility, peace, harmony, safety).
• - Poor menu.

```html
<!DOCTYPE html>
<html lang="pt">
<head>
<meta charset="utf-8">
<title>Norta Solução Cobrança</title>
<link href="https://fonts.googleapis.com/css2?family=Open+Sans:ital,wght@0,400;0,600;0,700;1,400&display=swap" rel="stylesheet">
<style>
:root{
  --navy:#1f2a5e;
  --ink:#222;
  --text:#666;
  --muted:#888;
  --footer:#2c2c2c;
  --footer-bar:#232323;
  --footer-text:#9a9a9a;
  --sky:#2f8dc6;
  --panel:#ececec;
}
*{box-sizing:border-box;margin:0;padding:0}
html,body{width:744px;height:1200px;overflow:hidden}
body{font-family:"Open Sans",Arial,sans-serif;background:#fff;color:var(--text);position:relative}
.abs{position:absolute}
a{color:inherit;text-decoration:none}

/* header */
.site-header{position:absolute;left:0;top:0;width:744px;height:66px;background:var(--navy)}
.brand{left:62px;top:12px;color:#fff;font-weight:700;line-height:1}
.brand .name{font-size:22px;letter-spacing:3px;display:block}
.brand .tag{font-size:6.5px;letter-spacing:1px;display:block;margin-top:6px}
.callus{left:434px;top:15px;font-size:7px;color:#fff;display:flex;align-items:center;gap:4px}
.login{left:592px;top:10px;width:91px;height:18px;border:1px solid #fff;border-radius:2px;color:#fff;font-size:7px;display:flex;align-items:center;justify-content:space-between;padding:0 6px}
.login span{display:flex;align-items:center;gap:4px}
.main-nav{left:288px;top:44px;width:396px;display:flex;justify-content:space-between;font-size:7px;color:#fff;font-weight:600}

/* hero */
.hero{left:0;top:66px;width:744px;height:286px;overflow:hidden;
  background:
    radial-gradient(ellipse 130px 170px at 600px 200px,rgba(60,80,110,.75),transparent 70%),
    radial-gradient(ellipse 110px 140px at 400px 230px,rgba(70,140,200,.7),transparent 70%),
    radial-gradient(ellipse 90px 120px at 460px 80px,rgba(20,150,210,.65),transparent 70%),
    radial-gradient(ellipse 60px 70px at 330px 80px,rgba(200,160,130,.55),transparent 70%),
    radial-gradient(ellipse 60px 70px at 530px 95px,rgba(190,145,115,.55),transparent 70%),
    radial-gradient(ellipse 160px 60px at 250px 270px,rgba(245,248,252,.85),transparent 70%),
    linear-gradient(100deg,#e4ebf0 0%,#c9d7e2 25%,#9fb6c9 50%,#6d8aa8 70%,#cfdae3 100%)}
.hero-title{left:72px;top:96px;font-size:17px;font-weight:700;color:var(--navy);line-height:22px}
.hero-btn{left:72px;top:146px;width:85px;height:28px;background:var(--navy);color:#fff;font-size:8px;font-weight:700;display:flex;align-items:center;justify-content:center;border-radius:2px}
.slide-arrow{top:134px;width:22px;height:22px;border-radius:50%;background:rgba(255,255,255,.25);display:flex;align-items:center;justify-content:center}

/* welcome */
.welcome-title{left:0;top:386px;width:744px;text-align:center;font-size:14.5px;font-weight:700;color:var(--ink)}
.welcome-sub{left:0;top:414px;width:744px;text-align:center;font-size:8.5px;color:#444}
.welcome-text{left:94px;top:436px;width:556px;text-align:center;font-size:6.3px;line-height:14.5px;color:var(--text)}

/* service cards */
.card{top:507px;width:193px}
.card .media{height:107px;border-radius:6px;box-shadow:0 6px 6px -3px rgba(0,0,0,.25)}
.card h3{font-size:7.5px;font-weight:700;color:var(--ink);margin-top:20px}
.card p{font-size:6.3px;line-height:14.3px;margin-top:5px}
.btn{display:inline-flex;align-items:center;justify-content:center;width:63px;height:19px;background:var(--navy);color:#fff;font-size:6.5px;border-radius:2px;box-shadow:0 3px 3px rgba(0,0,0,.25)}
.card .btn{margin-top:5px}

/* section row */
.col-title{top:762px;font-size:9.5px;font-weight:700;color:var(--ink)}
.news-item{left:62px;width:210px;display:flex;gap:13px}
.news-item .thumb{width:67px;height:46px;flex:none}
.news-item h4{font-size:6px;font-weight:700;color:var(--ink);line-height:12px;margin-top:3px}
.news-item time{font-size:6.5px;color:var(--muted);display:block;margin-top:3px}
.about{left:303px;top:792px;width:185px}
.about .media{height:84px}
.about p{font-size:6.3px;line-height:14.3px;margin-top:10px}
.about .btn{margin-top:8px}
.quote{left:513px;top:792px;width:170px;height:93px;background:var(--panel);border:1px solid #d8d8d8;border-radius:2px;padding:18px 14px 0 29px;font-size:6.3px;font-style:italic;line-height:13.3px;color:#777}
.quote-mark{font-family:Georgia,serif;font-size:16px;color:#bbb;font-style:normal}
.person-photo{left:520px;top:903px;width:44px;height:44px;border-radius:50%;border:2px solid #eee;background:radial-gradient(circle at 50% 40%,#e6cdb8 0 35%,#f2f2f2 36% 60%,#c8ccd2 61%)}
.person-name{left:572px;top:914px;font-size:6.5px;font-weight:700;color:#444}
.person-role{left:572px;top:926px;font-size:6.5px;color:var(--muted)}

/* footer */
.site-footer{left:0;top:1003px;width:744px;height:159px;background:var(--footer)}
.f-title{top:27px;font-size:8.5px;font-weight:700;color:#fff}
.f-text{font-size:6.3px;line-height:14.3px;color:var(--footer-text)}
.f-links{list-style:none;font-size:6.5px;color:var(--footer-text);line-height:17px}
.input{left:299px;top:78px;width:142px;height:17px;background:#fff;border-radius:2px;font-size:6.3px;color:#777;padding:4px 9px}
.subscribe{left:299px;top:103px;width:61px;height:19px;background:var(--sky);color:#fff;font-size:6.5px;display:flex;align-items:center;justify-content:center;border-radius:2px}
.bottom-bar{left:0;top:1162px;width:744px;height:38px;background:var(--footer-bar);font-size:6.5px;color:var(--footer-text)}
.social{left:481px;top:14px;display:flex;align-items:center;gap:12px}
.social i{width:7px;height:7px;border-radius:50%;background:#8a8a8a;display:block}
</style>
</head>
<body>

<header class="site-header">
  <div class="abs brand"><span class="name">NORTA</span><span class="tag">SOLUÇÃO COBRANÇA</span></div>
  <div class="abs callus">
    <svg width="8" height="8" viewBox="0 0 24 24"><path fill="#fff" d="M6.6 10.8a15 15 0 006.6 6.6l2.2-2.2c.3-.3.7-.4 1-.2 1.1.4 2.3.6 3.6.6.6 0 1 .4 1 1V20c0 .6-.4 1-1 1A17 17 0 013 4c0-.6.4-1 1-1h3.5c.6 0 1 .4 1 1 0 1.3.2 2.5.6 3.6.1.3 0 .7-.2 1z"/></svg>
    CALL US : (31) 3000 0123,&nbsp; (31) 7000 0456
  </div>
  <a class="abs login" href="#"><span><svg width="7" height="7" viewBox="0 0 24 24"><circle cx="12" cy="7" r="5" fill="#fff"/><path fill="#fff" d="M2 23c0-6 4.5-9 10-9s10 3 10 9z"/></svg>Members Login</span><svg width="6" height="4" viewBox="0 0 6 4"><path d="M0 0h6L3 4z" fill="#fff"/></svg></a>
  <nav class="abs main-nav"><a href="#">HOME</a><a href="#">ABOUT US</a><a href="#">SERVICES</a><a href="#">BLOG</a><a href="#">TESTIMONIALS</a><a href="#">CONTACT US</a></nav>
</header>

<section class="abs hero" role="img" aria-label="Photo of three colleagues working together at a laptop in a bright office">
  <div class="abs slide-arrow" style="left:8px"><svg width="7" height="9" viewBox="0 0 7 9"><path d="M5 1L1.5 4.5 5 8" stroke="#fff" fill="none" stroke-width="1.4"/></svg></div>
  <div class="abs slide-arrow" style="left:698px"><svg width="7" height="9" viewBox="0 0 7 9"><path d="M2 1l3.5 3.5L2 8" stroke="#fff" fill="none" stroke-width="1.4"/></svg></div>
  <h1 class="abs hero-title">COBRANÇA GARANTIDA<br>DE CONDOMÍNIO</h1>
  <a class="abs hero-btn" href="#">CLICK HERE</a>
</section>

<h2 class="abs welcome-title">WELCOME TO NORTA SOLUÇÃO COBRANÇA</h2>
<p class="abs welcome-sub">QUER RECEBER TODAS AS TAXAS DO SEU CONDOMÍNIO EM DIA E AINDA AUMENTAR SUA RECEITA?</p>
<p class="abs welcome-text">A NORTA SOLUÇÃO COBRANÇA é uma empresa que faz a cobrança do seu condomínio de forma diferente. Todo mês, na data de vencimento das taxas condominiais depositamos na conta bancária do condomínio o valor da receita total (descontada nossa taxa de serviço), efetuando posteriormente a cobrança daqueles que não pagaram em dia. Se algum condômino deixa de pagar, a NORTA assume essa obrigação e paga a taxa de condomínio por ele.</p>

<article class="abs card" style="left:62px">
  <div class="media" role="img" aria-label="Photo of a woman smiling on a sofa with a laptop" style="background:radial-gradient(ellipse 45px 50px at 95px 40px,rgba(110,70,45,.8),transparent 70%),radial-gradient(ellipse 55px 30px at 140px 80px,rgba(215,185,150,.9),transparent 70%),radial-gradient(ellipse 80px 40px at 60px 95px,rgba(120,120,115,.8),transparent 70%),linear-gradient(180deg,#d8d2ca,#a89d92 60%,#8f877f)"></div>
  <h3>REQUEST A PROPOSAL</h3>
  <p>A NORTA SOLUÇÃO COBRANÇA é uma empresa que faz a cobrança do seu condomínio de forma diferente. Todo mês, na data de vencimento...</p>
  <a class="btn" href="#">Read more</a>
</article>
<article class="abs card" style="left:276px">
  <div class="media" role="img" aria-label="Illustration of hands holding a tablet showing business charts" style="background:radial-gradient(ellipse 55px 45px at 100px 50px,rgba(40,70,110,.85),transparent 70%),radial-gradient(ellipse 60px 30px at 50px 90px,rgba(40,110,180,.7),transparent 70%),radial-gradient(ellipse 50px 40px at 170px 20px,rgba(255,255,255,.8),transparent 70%),linear-gradient(135deg,#e6eef6,#9fbcd9 50%,#dde8f2)"></div>
  <h3>RECOMMEND</h3>
  <p>A NORTA SOLUÇÃO COBRANÇA é uma empresa que faz a cobrança do seu condomínio de forma diferente. Todo mês, na data de vencimento...</p>
  <a class="btn" href="#">Read more</a>
</article>
<article class="abs card" style="left:490px">
  <div class="media" role="img" aria-label="Photo of hands typing on a keyboard at a wooden desk" style="background:radial-gradient(ellipse 40px 25px at 110px 80px,rgba(235,235,235,.95),transparent 70%),radial-gradient(ellipse 30px 55px at 15px 75px,rgba(60,65,75,.7),transparent 70%),linear-gradient(180deg,#f6f5f2 0%,#eeeae4 35%,#d2ab7c 45%,#c69a68 100%)"></div>
  <h3>CLASSIFIEDS</h3>
  <p>A NORTA SOLUÇÃO COBRANÇA é uma empresa que faz a cobrança do seu condomínio de forma diferente. Todo mês, na data de vencimento...</p>
  <a class="btn" href="#">Read more</a>
</article>

<h2 class="abs col-title" style="left:61px">NEWS / ARTICLES</h2>
<h2 class="abs col-title" style="left:302px">ABOUT&nbsp; NORTA SOLUÇÃO COBRANÇA</h2>
<h2 class="abs col-title" style="left:513px">TESTIMONIALS</h2>
<svg class="abs" style="left:667px;top:765px" width="14" height="6" viewBox="0 0 14 6"><path d="M3 0L0 3l3 3M11 0l3 3-3 3" fill="none" stroke="#aaa"/></svg>

<div class="abs news-item" style="top:792px">
  <div class="thumb" role="img" aria-label="Photo of a smiling businessman on the phone" style="background:radial-gradient(ellipse 18px 16px at 25px 20px,rgba(215,170,140,.9),transparent 70%),radial-gradient(ellipse 25px 14px at 35px 40px,rgba(240,240,240,.95),transparent 70%),linear-gradient(135deg,#e9edf1,#b9c4cf)"></div>
  <div><h4>BRASÍLIA RECEBE EVENTO SOBRE GESTÃO CONDOMINIAL EM JULHO</h4><time>Posted on 01/07/2015</time></div>
</div>
<div class="abs news-item" style="top:854px">
  <div class="thumb" role="img" aria-label="Photo of a woman working at a desk by a window" style="background:radial-gradient(ellipse 14px 20px at 40px 22px,rgba(140,110,90,.7),transparent 70%),linear-gradient(90deg,#8a9690 0%,#d7dcdd 40%,#f3f4f4 100%)"></div>
  <div><h4>BRASÍLIA RECEBE EVENTO SOBRE GESTÃO CONDOMINIAL EM JULHO</h4><time>Posted on 01/07/2015</time></div>
</div>
<div class="abs news-item" style="top:916px">
  <div class="thumb" role="img" aria-label="Photo of a business team in an office" style="background:radial-gradient(ellipse 16px 24px at 15px 30px,rgba(40,40,50,.85),transparent 70%),radial-gradient(ellipse 16px 22px at 50px 22px,rgba(200,150,110,.9),transparent 70%),linear-gradient(135deg,#b58a64,#e9e3dc)"></div>
  <div><h4>BRASÍLIA RECEBE EVENTO SOBRE GESTÃO CONDOMINIAL EM JULHO</h4><time>Posted on 01/07/2015</time></div>
</div>

<div class="abs about">
  <div class="media" role="img" aria-label="Photo of business people in a meeting" style="background:radial-gradient(ellipse 30px 40px at 70px 55px,rgba(40,40,50,.85),transparent 70%),radial-gradient(ellipse 30px 40px at 130px 45px,rgba(210,170,140,.85),transparent 70%),radial-gradient(ellipse 25px 35px at 30px 60px,rgba(90,95,110,.8),transparent 70%),linear-gradient(180deg,#e3e6ea,#b8bcc2 60%,#8d9097)"></div>
  <p>A NORTA SOLUÇÃO COBRANÇA é uma empresa que faz a cobrança do seu condomínio de forma diferente. Todo mês, na data de vencimento...</p>
  <a class="btn" href="#">Read more</a>
</div>

<blockquote class="abs quote">
  <span class="abs quote-mark" style="left:14px;top:12px">&ldquo;</span>
  Lorem Ipsum is simply dummy text of the printing and typesetting industry. Lorem Ipsum has been the industry's standard dummy text ever...
  <span class="abs quote-mark" style="left:150px;top:68px">&rdquo;</span>
</blockquote>
<svg class="abs" style="left:640px;top:884px" width="20" height="20" viewBox="0 0 20 20"><path d="M0 0h20L2 18z" fill="var(--panel)" stroke="#d8d8d8"/><path d="M0 0h20" stroke="var(--panel)" stroke-width="2"/></svg>
<div class="abs person-photo" role="img" aria-label="Portrait photo of the client giving the testimonial"></div>
<div class="abs person-name">CAIO MENDES</div>
<div class="abs person-role">Business man</div>

<footer class="abs site-footer">
  <h3 class="abs f-title" style="left:62px">SUCCESSFUL STORIES</h3>
  <p class="abs f-text" style="left:62px;top:49px;width:210px">Lorem Ipsum is simply dummy text of the printing and typesetting industry. Lorem Ipsum has been the industry's standard dummy text ever since the 1500s...</p>
  <a class="abs" href="#" style="left:63px;top:96px;font-size:6.5px;color:#ddd;font-weight:600;display:flex;align-items:center;gap:4px">Read more info <svg width="7" height="7" viewBox="0 0 10 10"><circle cx="5" cy="5" r="5" fill="#999"/><path d="M4 3l2 2-2 2" stroke="#2c2c2c" fill="none" stroke-width="1.3"/></svg></a>
  <div class="abs" style="left:63px;top:118px;width:24px;height:24px;border-radius:50%;background:#555"></div>

  <h3 class="abs f-title" style="left:299px">NEWSLETTER SIGNUP</h3>
  <p class="abs f-text" style="left:299px;top:47px;width:140px">Get our recent updates through your email id</p>
  <div class="abs input">Enter your email id</div>
  <a class="abs subscribe" href="#">Subscribe</a>

  <h3 class="abs f-title" style="left:479px">WELCOME</h3>
  <ul class="abs f-links" style="left:479px;top:46px"><li>Home</li><li>About Us</li><li>Services</li><li>Blog</li><li>Testimonials</li><li>Contact Us</li></ul>

  <h3 class="abs f-title" style="left:575px">CONTACT INFO</h3>
  <p class="abs f-text" style="left:575px;top:49px">120 Street name, City name,<br>Country name : 3652235</p>
  <svg class="abs" style="left:578px;top:82px" width="7" height="7" viewBox="0 0 24 24"><path fill="#9a9a9a" d="M6.6 10.8a15 15 0 006.6 6.6l2.2-2.2c.3-.3.7-.4 1-.2 1.1.4 2.3.6 3.6.6.6 0 1 .4 1 1V20c0 .6-.4 1-1 1A17 17 0 013 4c0-.6.4-1 1-1h3.5c.6 0 1 .4 1 1 0 1.3.2 2.5.6 3.6.1.3 0 .7-.2 1z"/></svg>
  <p class="abs f-text" style="left:590px;top:80px;line-height:12.5px">(31) 3000 0123<br>(31) 7000 0456</p>
  <svg class="abs" style="left:577px;top:111px" width="8" height="6" viewBox="0 0 8 6"><rect width="8" height="6" fill="#9a9a9a"/><path d="M0 0l4 3 4-3" stroke="#2c2c2c" fill="none" stroke-width=".8"/></svg>
  <p class="abs f-text" style="left:590px;top:106px">contato@nortacobranca.com.br</p>
</footer>

<div class="abs bottom-bar">
  <span class="abs" style="left:62px;top:14px">© 2015. NORTA. All rights reserved</span>
  <div class="abs social"><span>Connct with our social network :</span><i></i><i></i><i></i><i></i><i></i></div>
</div>

</body>
</html>
```